Industrial Automation PowerPoint Brochure

I am looking for a powerpoint brochure that captures our corporate culture, logo and mission statemente (Intelligence, Ingenuity, Integrity).

I have some examples of past brochures uses however I am hoping for a more modern and appealing layout and look. '

www.brindlecontrols.ca

```html
<!DOCTYPE html>
<html lang="en">
<head>
<meta charset="utf-8">
<title>Brindle Controls – Fabrication</title>
<link rel="stylesheet" href="https://fonts.googleapis.com/css2?family=Carlito:wght@400;700&family=Open+Sans:wght@400;500;600&display=swap">
<style>
  :root {
    --band-top: #d4e8c2;
    --band-bottom: #9dd266;
    --band-bottom-deep: #7fbf45;
    --title-blue: #2e5597;
    --ink: #1e1e1e;
    --accent-orange: #c55a11;
    --accent-red: #c00000;
    --paper: #f1f2ef;
    --badge: #ffffff;
    --on-green: #ffffff;
  }
  * { box-sizing: border-box; margin: 0; padding: 0; }
  html, body { width: 900px; height: 1200px; overflow: hidden; }
  body { background: var(--paper); font-family: "Open Sans", Verdana, sans-serif; color: var(--ink); }
  .brochure-page { position: relative; width: 900px; height: 1200px; overflow: hidden; }

  .workshop-backdrop {
    position: absolute; left: 0; top: 0; width: 900px; height: 1110px;
    background:
      radial-gradient(ellipse 320px 380px at 120px 620px, rgba(250,232,170,0.75), transparent 70%),
      radial-gradient(ellipse 420px 520px at 640px 820px, rgba(196,214,170,0.7), transparent 72%),
      linear-gradient(180deg, #f4f4f2 0%, #ecedea 45%, #e6e9df 100%);
  }

  .band-top { position: absolute; left: 0; top: 0; width: 900px; height: 62px; background: var(--band-top); }
  .brand {
    position: absolute; left: 36px; top: 17px;
    display: flex; align-items: center; gap: 10px;
    font-family: "Carlito", Calibri, sans-serif; font-weight: 700;
    font-size: 24px; line-height: 28px; color: var(--title-blue);
  }
  .brand-dot { width: 20px; height: 20px; border-radius: 50%; background: var(--title-blue); }

  .page-title {
    position: absolute; right: 20px; top: 40px;
    font-family: "Open Sans", sans-serif; font-weight: 500;
    font-size: 76px; letter-spacing: 6px; color: var(--title-blue); line-height: 1;
  }

  .intro {
    position: absolute; left: 46px; top: 176px; width: 828px;
    font-size: 19.5px; line-height: 28.6px; letter-spacing: 0.45px; text-align: justify;
  }
  .intro .highlight { color: var(--accent-red); font-size: 25px; letter-spacing: 0.5px; font-family: "Carlito", Calibri, sans-serif; }

  .section { position: absolute; font-family: "Carlito", Calibri, sans-serif; }
  .section h2 { font-weight: 400; font-size: 33px; line-height: 40px; color: var(--ink); margin-bottom: 6px; }
  .section ul { list-style: none; }
  .section li { position: relative; padding-left: 38px; font-size: 23px; line-height: 28.6px; color: var(--accent-orange); }
  .section li::before { content: "•"; position: absolute; left: 12px; top: 0; }
  .capabilities { left: 36px; top: 398px; }
  .facility { left: 353px; top: 392px; }
  .market { left: 36px; top: 700px; }

  .badge { position: absolute; width: 150px; height: 150px; background: var(--badge); border-radius: 50% 0 50% 50%; }
  .badge-1 { left: 373px; top: 662px; }
  .badge-2 { left: 611px; top: 659px; }
  .badge-3 { left: 348px; top: 862px; }
  .badge-4 { left: 610px; top: 866px; }

  .band-bottom {
    position: absolute; left: 0; top: 1109px; width: 900px; height: 91px;
    background: var(--band-bottom);
    display: flex; align-items: center; justify-content: space-between;
    padding: 0 36px;
    font-family: "Carlito", Calibri, sans-serif; color: var(--on-green);
  }
  .mission { font-size: 28px; font-weight: 700; letter-spacing: 1px; }
  .mission .sep { display: inline-block; width: 8px; height: 8px; border-radius: 50%; background: var(--on-green); margin: 0 14px; vertical-align: middle; }
  .website { font-size: 22px; letter-spacing: 0.5px; }
</style>
</head>
<body>
<main class="brochure-page">
  <div class="workshop-backdrop" role="img" aria-label="Faded photograph of the fabrication workshop floor with green cable reels"></div>

  <div class="band-top"></div>
  <div class="brand"><span class="brand-dot"></span>Brindle Controls</div>
  <h1 class="page-title">FABRICATION</h1>

  <p class="intro">Brindle Controls’ fabrication facility is located in Edmonton, Alberta, in the same complex as our engineering office. Direct access to our automation &amp; engineering team raises project quality and fabrication efficiency. As added value to our clients, who have come to expect the highest quality in the industry, we maintain a fully <span class="highlight">trained and certified</span> journeyman electrical staff. This ensures no gaps for our clients and their prospective projects.</p>

  <section class="section capabilities">
    <h2>Capabilities</h2>
    <ul>
      <li>Control Panels</li>
      <li>PLC Control Panels</li>
      <li>RTU Panels</li>
      <li>Marshalling Cabinets</li>
      <li>Junction Boxes</li>
      <li>VFD Panels</li>
      <li>SCADA Panels</li>
    </ul>
  </section>

  <section class="section facility">
    <h2>Facility</h2>
    <ul>
      <li>24/7 Access</li>
      <li>Live Streaming Video</li>
      <li>Forklift / Large Bay Door</li>
      <li>4,000 sq/ft</li>
      <li>Engineering / Fabrication</li>
      <li>Cloud-Based Quality Program</li>
    </ul>
  </section>

  <section class="section market">
    <h2>Market</h2>
    <ul>
      <li>Oil &amp; Gas</li>
      <li>Pipeline</li>
      <li>Mining</li>
      <li>Drilling</li>
      <li>Chemical</li>
      <li>Agriculture</li>
      <li>Forestry</li>
      <li>Municipalities</li>
    </ul>
  </section>

  <div class="badge badge-1" aria-hidden="true"></div>
  <div class="badge badge-2" aria-hidden="true"></div>
  <div class="badge badge-3" aria-hidden="true"></div>
  <div class="badge badge-4" aria-hidden="true"></div>

  <footer class="band-bottom">
    <p class="mission">Intelligence<span class="sep"></span>Ingenuity<span class="sep"></span>Integrity</p>
    <p class="website">www.brindlecontrols.ca</p>
  </footer>
</main>
</body>
</html>
```